Tri-fold discount dental plan brochure
We need a standard Tri-fold brochure for our discount dental membership plan. Attached is a Word documents which contains the text for the brochure.
Health
Please use the text that is provided in the word document attached. Also pictures can be used form pictovanta.com and we will purchase them later on.
logo
content and copy can be download here.
pleasse get the chart and application from these files

```html
<!DOCTYPE html>
<html lang="en">
<head>
<meta charset="utf-8">
<title>RQO Dental – Tri-fold Brochure</title>
<link href="https://fonts.googleapis.com/css2?family=Open+Sans:wght@400;600;700&display=swap" rel="stylesheet">
<style>
:root{
  --bg:#e6ebf0;
  --blue:#1b6db3;
  --blue-dark:#0e4d8a;
  --blue-light:#5aa9e0;
  --sky:#dcecf8;
  --paper:#ffffff;
  --ink:#2b3a4a;
  --muted:#6c7b8a;
  --green:#9ccb5b;
  --photo-a:#c9b29a;
  --photo-b:#e8d6c2;
}
*{box-sizing:border-box;margin:0;padding:0}
html,body{width:1200px;height:1037px;overflow:hidden}
body{background:var(--bg);font-family:"Open Sans",Arial,sans-serif;color:var(--ink);position:relative}
.sheet{position:absolute;left:30px;width:1140px;height:470px;display:flex;box-shadow:0 4px 14px rgba(0,0,0,.15)}
.sheet.outside{top:30px}
.sheet.inside{top:537px}
.panel{width:380px;height:100%;position:relative;overflow:hidden;background:var(--paper)}
.panel+.panel{border-left:1px dashed #c5d0da}
.photo{background:linear-gradient(135deg,var(--photo-b),var(--photo-a));border-radius:10px}
.photo.brush{background:linear-gradient(135deg,#f4f8fb,#cfe6f6 55%,var(--green))}
.band{background:linear-gradient(180deg,var(--blue-light),var(--blue))}
/* How it works */
.how{background:linear-gradient(180deg,var(--blue),var(--blue-dark));color:#fff;padding:28px 26px}
.how h2{font-size:22px;font-weight:700;margin-bottom:14px}
.how ul{list-style:none}
.how li{font-size:12.5px;line-height:1.45;margin-bottom:9px;padding-left:16px;position:relative}
.how li::before{content:"";position:absolute;left:0;top:6px;width:7px;height:7px;border-radius:50%;background:var(--blue-light)}
.how .photo{position:absolute;left:26px;right:26px;bottom:24px;height:120px}
/* Testimonials */
.voices .photo{margin:22px 22px 0;height:150px}
.voices h2{color:var(--blue);font-size:19px;margin:16px 22px 10px}
.quote{margin:0 22px 10px;font-size:12px;line-height:1.45;font-style:italic;color:var(--ink)}
.quote b{display:block;font-style:normal;font-weight:600;color:var(--blue);font-size:11px;margin-top:2px}
.voices .band{position:absolute;left:0;right:0;bottom:0;height:18px}
/* Cover */
.cover{background:linear-gradient(180deg,#fff 0,#fff 60%,var(--sky))}
.brand{display:flex;align-items:center;gap:10px;justify-content:center;margin-top:32px}
.brand .dot{width:12px;height:12px;border-radius:50%;background:var(--blue)}
.brand .name{font-size:26px;font-weight:600;color:var(--blue)}
.tagline{text-align:center;font-size:11px;color:var(--muted);margin-top:4px}
.cover .photo.main{margin:22px 26px 0;height:150px}
.cover .photo.brush{margin:14px 26px 0;height:86px}
.call{position:absolute;left:0;right:0;bottom:0;height:86px;color:#fff;text-align:center;padding-top:16px;border-radius:40px 40px 0 0}
.call p{font-size:14px;font-style:italic}
.call strong{display:block;font-size:26px;font-weight:700;letter-spacing:.5px}
/* Inside: why */
.why .photo{margin:22px 22px 0;height:140px}
.why h2{color:var(--blue);font-size:19px;margin:16px 22px 8px}
.why p{font-size:12.5px;line-height:1.5;margin:0 22px 10px}
.why ul{list-style:none;margin:0 22px}
.why li{font-size:12.5px;line-height:1.4;margin-bottom:6px;display:flex;align-items:center;gap:8px}
.why svg{flex:none}
/* Inside: fees */
.fees h2{background:var(--blue);color:#fff;font-size:17px;padding:12px 20px}
.fees .photo{margin:16px 20px 12px;height:110px}
table{border-collapse:collapse;margin:0 20px;width:340px;font-size:12px}
th{background:var(--blue-light);color:#fff;text-align:left;padding:6px 8px;font-weight:600}
td{padding:6px 8px;border-bottom:1px solid #d9e3ec}
tr:nth-child(even) td{background:var(--sky)}
td.num,th.num{text-align:right}
/* Inside: application */
.apply{padding:20px 22px}
.apply h2{color:var(--blue);font-size:20px;margin-bottom:10px}
.field{display:flex;gap:6px;font-size:11.5px;margin-bottom:9px;align-items:flex-end}
.field span{white-space:nowrap}
.field i{flex:1;border-bottom:1px solid #9fb2c4;height:14px}
.field.sign{margin-top:12px}
.apply h3{font-size:13px;color:var(--blue-dark);margin:12px 0 8px}
.checks{display:flex;gap:16px;font-size:11.5px;margin-bottom:6px}
.checks span::before{content:"";display:inline-block;width:10px;height:10px;border:1px solid var(--blue);margin-right:5px;vertical-align:-1px}
</style>
</head>
<body>

<section class="sheet outside">
  <div class="panel how">
    <h2>How Does It Work?</h2>
    <ul>
      <li>Pick the plan that suits your household and enroll online or by phone.</li>
      <li>Receive your member card and welcome kit within days.</li>
      <li>Visit any participating dentist and show your card.</li>
      <li>Pay the reduced fee at the time of your visit.</li>
      <li>Save on cleanings, fillings, crowns and more.</li>
    </ul>
    <div class="photo" role="img" aria-label="Photo of a smiling woman at the dentist"></div>
  </div>

  <div class="panel voices">
    <div class="photo" role="img" aria-label="Photo of a smiling family"></div>
    <h2>What Our Customers Are Saying</h2>
    <p class="quote">"I saved hundreds on my crown the very first month. Signing up was simple."<b>— Maria T.</b></p>
    <p class="quote">"Our whole family is covered for less than one dinner out each month."<b>— James R.</b></p>
    <p class="quote">"Finding a dentist nearby took minutes and the staff were friendly."<b>— Linda K.</b></p>
    <div class="band"></div>
  </div>

  <div class="panel cover">
    <div class="brand"><span class="dot"></span><span class="name">RQO Dental</span></div>
    <p class="tagline">Affordable care for every smile</p>
    <div class="photo main" role="img" aria-label="Photo of a smiling senior couple"></div>
    <div class="photo brush" role="img" aria-label="Photo of a toothbrush with toothpaste"></div>
    <div class="call band"><p>Call RQO Dental today on</p><strong>1.800.555.0142</strong></div>
  </div>
</section>

<section class="sheet inside">
  <div class="panel why">
    <div class="photo" role="img" aria-label="Photo of a smiling mother and child"></div>
    <h2>Why Choose RQO Dental</h2>
    <p>RQO Dental is a discount membership that lowers what you pay at the dentist. There are no waiting periods, no yearly limits and no paperwork.</p>
    <ul>
      <li><svg width="14" height="14" viewBox="0 0 14 14"><path d="M2 7l3 3 7-7" fill="none" stroke="#1b6db3" stroke-width="2"/></svg>No waiting periods</li>
      <li><svg width="14" height="14" viewBox="0 0 14 14"><path d="M2 7l3 3 7-7" fill="none" stroke="#1b6db3" stroke-width="2"/></svg>No annual maximums</li>
      <li><svg width="14" height="14" viewBox="0 0 14 14"><path d="M2 7l3 3 7-7" fill="none" stroke="#1b6db3" stroke-width="2"/></svg>Pre-existing conditions accepted</li>
      <li><svg width="14" height="14" viewBox="0 0 14 14"><path d="M2 7l3 3 7-7" fill="none" stroke="#1b6db3" stroke-width="2"/></svg>Plans for singles and families</li>
    </ul>
  </div>

  <div class="panel fees">
    <h2>Dental Plan Fee Schedule</h2>
    <div class="photo" role="img" aria-label="Photo of a smiling young family"></div>
    <table>
      <tr><th>Procedure</th><th class="num">Usual Fee</th><th class="num">Member Fee</th></tr>
      <tr><td>Routine Exam</td><td class="num">$65</td><td class="num">$20</td></tr>
      <tr><td>Cleaning (Adult)</td><td class="num">$95</td><td class="num">$35</td></tr>
      <tr><td>Full-mouth X-rays</td><td class="num">$120</td><td class="num">$45</td></tr>
      <tr><td>Filling (Amalgam)</td><td class="num">$150</td><td class="num">$60</td></tr>
      <tr><td>Root Canal (Molar)</td><td class="num">$1,100</td><td class="num">$520</td></tr>
      <tr><td>Crown (Porcelain)</td><td class="num">$1,250</td><td class="num">$575</td></tr>
      <tr><td>Simple Extraction</td><td class="num">$180</td><td class="num">$70</td></tr>
    </table>
  </div>

  <div class="panel apply">
    <h2>Application</h2>
    <div class="field"><span>Name</span><i></i></div>
    <div class="field"><span>Address</span><i></i></div>
    <div class="field"><span>City</span><i></i><span>State</span><i></i><span>Zip</span><i></i></div>
    <div class="field"><span>Phone</span><i></i><span>Date of Birth</span><i></i></div>
    <div class="field"><span>Email</span><i></i></div>
    <h3>Additional Household Family Members</h3>
    <div class="field"><span>1.</span><i></i></div>
    <div class="field"><span>2.</span><i></i></div>
    <div class="field"><span>3.</span><i></i></div>
    <h3>Type of Membership</h3>
    <div class="checks"><span>Individual</span><span>Couple</span><span>Family</span></div>
    <h3>Payment Type</h3>
    <div class="checks"><span>Credit Card</span><span>Check</span></div>
    <div class="field sign"><span>Signature</span><i></i><span>Date</span><i></i></div>
  </div>
</section>

</body>
</html>
```